New Business Card (to reflect updated website content and graphics)

I changed some text and graphics on my website, so I need a new business card.

Target Market(s)

Mostly women, ages 30 - 60.

Industry/Entity Type

Life Coaching

Contact Information for Business Card

Included in attached Word document

Font styles to use
Sans Serif

Requirements
Must have
• I am not a creative person, so I will defer to designer. Take a look at my website, and you can get a feel for me, my style, and my target audience. Thank You!

My 3 branding colors are included in attached Word document.

```html
<!DOCTYPE html>
<html lang="en">
<head>
<meta charset="UTF-8">
<title>Harbor Heart Coaching – Business Card</title>
<link href="https://fonts.googleapis.com/css2?family=Montserrat:wght@700&family=Open+Sans:wght@400;600&display=swap" rel="stylesheet">
<style>
  :root {
    --teal: #2a93b4;
    --teal-tint: #d7ebf1;
    --ink: #4d4d4d;
    --card: #ffffff;
    --backdrop: #e9ebee;
  }
  * { box-sizing: border-box; margin: 0; padding: 0; }
  html, body {
    width: 1200px; height: 800px; overflow: hidden;
    background: var(--backdrop);
    font-family: "Open Sans", Arial, sans-serif;
  }
  .sheet {
    width: 1200px; height: 800px;
    display: flex; align-items: center; justify-content: center; gap: 40px;
  }
  .card {
    width: 540px; height: 309px;
    background: var(--card);
    box-shadow: 0 6px 20px rgba(0,0,0,0.12);
    position: relative;
    overflow: hidden;
  }
  /* Front */
  .card-front { display: flex; align-items: center; justify-content: center; }
  .front-artwork {
    width: 190px; height: 150px;
    margin-top: -30px;
    border-radius: 6px;
    background: var(--teal-tint);
  }
  /* Back */
  .card-back { display: flex; align-items: center; }
  .brand {
    width: 238px; padding-left: 44px; padding-right: 16px;
    display: flex; align-items: center; gap: 10px;
  }
  .brand-dot {
    width: 12px; height: 12px; border-radius: 50%;
    background: var(--teal); flex: none;
  }
  .brand-name {
    font-weight: 600; font-size: 21px; line-height: 1.25;
    color: var(--teal);
  }
  .divider {
    width: 1.5px; height: 150px; background: var(--teal);
    margin-right: 24px; flex: none;
  }
  .details { color: var(--ink); }
  .person-name {
    font-family: "Montserrat", Arial, sans-serif;
    font-weight: 700; font-size: 19px; letter-spacing: 0.3px;
    color: var(--teal); text-transform: uppercase;
    margin-bottom: 6px;
  }
  .roles { list-style: none; font-size: 11.5px; line-height: 1.5; margin-bottom: 14px; }
  .contacts { list-style: none; font-size: 11.5px; line-height: 1.75; }
  .contacts li { display: flex; align-items: center; gap: 8px; }
  .contacts svg { width: 11px; height: 11px; flex: none; fill: var(--teal); }
  .web-domain { color: var(--teal); }
</style>
</head>
<body>
<main class="sheet">
  <section class="card card-front">
    <div class="front-artwork" role="img" aria-label="Heart-shaped word cloud artwork with coaching words and a wellness tagline"></div>
  </section>

  <section class="card card-back">
    <div class="brand">
      <span class="brand-dot"></span>
      <span class="brand-name">Harbor Heart Coaching</span>
    </div>
    <div class="divider"></div>
    <div class="details">
      <h1 class="person-name">Maren Whitfield</h1>
      <ul class="roles">
        <li>Certified Professional Life Coach</li>
        <li>Health &amp; Wellness Coach</li>
        <li>Advanced Grief Support Specialist</li>
      </ul>
      <ul class="contacts">
        <li>
          <svg viewBox="0 0 24 24" aria-hidden="true"><path d="M6.6 10.8a15.1 15.1 0 0 0 6.6 6.6l2.2-2.2a1 1 0 0 1 1-.25 11.4 11.4 0 0 0 3.6.57 1 1 0 0 1 1 1V20a1 1 0 0 1-1 1A17 17 0 0 1 3 4a1 1 0 0 1 1-1h3.5a1 1 0 0 1 1 1c0 1.25.2 2.45.57 3.6a1 1 0 0 1-.25 1z"/></svg>
          (555) 214-3390
        </li>
        <li>
          <svg viewBox="0 0 24 24" aria-hidden="true"><path d="M2 5h20v14H2z M2 5l10 8 10-8" stroke="#fff" stroke-width="1.5"/></svg>
          maren@harborheartcoaching.com
        </li>
        <li>
          <svg viewBox="0 0 24 24" aria-hidden="true"><circle cx="12" cy="12" r="10"/><path d="M2 12h20M12 2c3 3 3 17 0 20M12 2c-3 3-3 17 0 20" stroke="#fff" stroke-width="1.3" fill="none"/></svg>
          <span>www.<span class="web-domain">harborheartcoaching</span>.com</span>
        </li>
      </ul>
    </div>
  </section>
</main>
</body>
</html>
```